Granite Ridge Holdings

I have a real estate investment business.

** I need editable vector files of the final design.

Industry/Entity Type

Real Estate

Contact Information for Business Card

I would like the card to be clear and direct with the company name and contact info. I would prefer not to have a design that is too busy (i.e., with excessive detail) in the business card.

Font styles to use
Sans Serif

Requirements
Must have
• My card must have the following information listed below:
• Company name: Grainite Ridge Holdings LLC
• My name: Daniel Vorsley
• Phone number: (555) 218-9067
• Email address: dtvorsley@mailbox-example.net
• Keywords: “Real Estate Investments”
Nice to have
• I would like to have a design that resembles the characteristics/uses of obsidian stone which resembles something related to strength and resilience. Perhaps something with sharp, sleek color transitions as well.

```html
<!DOCTYPE html>
<html lang="en">
<head>
<meta charset="UTF-8">
<title>Granite Ridge Holdings – Business Card</title>
<link href="https://fonts.googleapis.com/css2?family=Lato:ital,wght@0,400;0,700;1,400&display=swap" rel="stylesheet">
<style>
  :root {
    --brand-blue: #1121d6;
    --ink: #2a2a2a;
    --paper: #ffffff;
    --stone-dark: #0d0d0e;
    --stone-mid: #2b2b2e;
    --stone-light: #4a4a4e;
    --on-stone: #ffffff;
  }
  * { margin: 0; padding: 0; box-sizing: border-box; }
  html, body {
    width: 800px;
    height: 1200px;
    overflow: hidden;
    background: var(--paper);
  }
  .card {
    position: relative;
    width: 800px;
    height: 1200px;
    background: var(--paper);
    font-family: 'Lato', sans-serif;
    text-align: center;
  }
  .stone-band {
    position: absolute;
    left: 0;
    width: 800px;
    background:
      linear-gradient(125deg, transparent 0 30%, rgba(255,255,255,0.08) 31% 33%, transparent 34% 100%),
      linear-gradient(60deg, transparent 0 55%, rgba(255,255,255,0.07) 56% 58%, transparent 59% 100%),
      linear-gradient(160deg, var(--stone-mid) 0%, var(--stone-dark) 35%, var(--stone-light) 55%, var(--stone-dark) 75%, var(--stone-mid) 100%);
  }
  .stone-band--top { top: 0; height: 150px; }
  .stone-band--bottom { top: 900px; height: 300px; }
  .company-name {
    position: absolute;
    top: 58px;
    left: 0;
    width: 800px;
    font-size: 28px;
    font-weight: 700;
    letter-spacing: 0.36em;
    padding-left: 0.36em;
    color: var(--brand-blue);
    text-transform: uppercase;
    white-space: nowrap;
  }
  .person-name {
    position: absolute;
    top: 310px;
    left: 0;
    width: 800px;
    font-size: 55px;
    font-weight: 700;
    color: var(--brand-blue);
    text-transform: uppercase;
    letter-spacing: 0.02em;
  }
  .divider {
    position: absolute;
    top: 427px;
    left: 362px;
    width: 76px;
    height: 9px;
    background: var(--brand-blue);
  }
  .contact-icon {
    position: absolute;
    left: 386px;
    width: 28px;
    height: 28px;
  }
  .contact-icon--phone { top: 507px; }
  .contact-icon--mail { top: 700px; }
  .contact-label {
    position: absolute;
    left: 0;
    width: 800px;
    font-size: 22px;
    color: var(--brand-blue);
  }
  .contact-value {
    position: absolute;
    left: 0;
    width: 800px;
    font-size: 22px;
    color: var(--ink);
  }
  .label-phone { top: 571px; }
  .value-phone { top: 613px; }
  .label-mail { top: 735px; }
  .value-mail { top: 779px; }
  .tagline {
    position: absolute;
    top: 1106px;
    left: 0;
    width: 800px;
    font-size: 27px;
    font-style: italic;
    color: var(--on-stone);
  }
</style>
</head>
<body>
  <div class="card">
    <div class="stone-band stone-band--top" role="img" aria-label="Black crystalline obsidian stone texture"></div>
    <div class="company-name">Grainite Ridge Holdings LLC</div>

    <h1 class="person-name">Daniel Vorsley</h1>
    <div class="divider"></div>

    <svg class="contact-icon contact-icon--phone" viewBox="0 0 28 28" fill="none" stroke="var(--brand-blue)" stroke-width="1.2" aria-hidden="true">
      <path d="M7 3.5 L10.5 8 L8.6 10.4 C10 13.6 13.6 17.6 17.4 19.3 L19.8 17.4 L24.3 20.9 L22 24.3 C14 24 4.3 14.5 3.7 5.9 Z" stroke-linejoin="round"/>
    </svg>
    <div class="contact-label label-phone">Phone:</div>
    <div class="contact-value value-phone">(555) 218-9067</div>

    <svg class="contact-icon contact-icon--mail" viewBox="0 0 28 28" fill="none" stroke="var(--brand-blue)" stroke-width="1.3" aria-hidden="true">
      <rect x="2" y="6" width="24" height="17"/>
      <path d="M2 6 L14 16 L26 6"/>
      <path d="M2 23 L11 13.5 M26 23 L17 13.5"/>
    </svg>
    <div class="contact-label label-mail">E-mail:</div>
    <div class="contact-value value-mail">dtvorsley@mailbox-example.net</div>

    <div class="stone-band stone-band--bottom" role="img" aria-label="Black crystalline obsidian stone texture"></div>
    <div class="tagline">Real Estate Investments</div>
  </div>
</body>
</html>
```